CBD Oil manufacturer needs a label/logo.

We need a label/logo design for our CBD oil bottles. The brand name is Velsora - meaning immortality. CBD oil is made from the hemp plant, usually used medicinally. We are open to color schemes and designs. I am attaching a label that someone else made - but we do not like at all. The information listed on the side does need to be included.

Target Market(s)

CBD Oil Retailers - generally for medicinal purposes. Geared towards all ages, etc.

Industry/Entity Type

Manufacturer

Requirements
Must have
• Supplement Facts, Suggested use, Other Ingredients, Manufactured by, etc. AS SEEN ON ATTACHMENT.

```html
<!DOCTYPE html>
<html lang="en">
<head>
<meta charset="utf-8">
<title>Velsora Hemp Tincture Label</title>
<link href="https://fonts.googleapis.com/css2?family=Josefin+Sans:wght@400;600;700&family=Libre+Baskerville&family=Source+Serif+4:wght@400;700&display=swap" rel="stylesheet">
<style>
  :root {
    --backdrop: #e6e6e6;
    --paper: #ffffff;
    --ink: #141414;
    --ink-soft: #3a3a3a;
    --rule: #555555;
    --leaf-deep: #2f8a3c;
    --leaf-mid: #5aa64a;
    --leaf-light: #9fd067;
    --drip-lime: #c6e23a;
    --drip-pale: #e3f08a;
  }
  * { box-sizing: border-box; margin: 0; padding: 0; }
  html, body { width: 1200px; height: 418px; overflow: hidden; }
  body { background: var(--backdrop); position: relative; color: var(--ink); }

  .label { position: absolute; top: 54px; height: 310px; background: var(--paper); overflow: hidden; }

  /* Front label */
  .front-label { left: 54px; width: 572px; }
  .front-art { position: absolute; inset: 0; width: 100%; height: 100%; }
  .front-text { position: absolute; inset: 0; text-align: center; }
  .kicker {
    position: absolute; left: 0; right: 0; line-height: 1;
    font-family: "Libre Baskerville", serif; font-size: 15px;
    letter-spacing: 0.62em; padding-left: 0.62em;
  }
  .kicker-hemp { top: 59px; }
  .kicker-tincture { top: 200px; }
  .brand-name {
    position: absolute; left: 0; right: 0; top: 121px;
    font-family: "Josefin Sans", sans-serif; font-weight: 400; font-size: 42px;
    letter-spacing: 0.74em; padding-left: 0.74em; line-height: 1;
  }
  .product-lines {
    position: absolute; left: 0; right: 0; top: 258px;
    font-family: "Josefin Sans", sans-serif; font-weight: 700; font-size: 7.6px;
    letter-spacing: 0.12em; line-height: 13px;
  }

  /* Back label */
  .back-label { left: 638px; width: 179px; font-family: "Source Serif 4", serif; font-size: 4.4px; line-height: 1.25; }
  .back-label .block { position: absolute; }
  .section-title {
    font-family: "Josefin Sans", sans-serif; font-weight: 700; font-size: 4.9px;
    letter-spacing: 0.13em; white-space: nowrap; line-height: 1;
  }
  .facts { left: 13px; top: 33px; width: 156px; }
  .facts .section-title { margin-bottom: 7px; }
  .facts .serving { margin-bottom: 6px; white-space: nowrap; }
  .facts .serving b { font-weight: 700; }
  .facts .serving span { margin-right: 7px; }
  .facts-table { width: 100%; border-collapse: collapse; }
  .facts-table th { font-weight: 700; text-align: center; padding-bottom: 3.5px; border-bottom: 0.7px solid var(--rule); }
  .facts-table td { padding: 2.4px 0 2.4px; vertical-align: top; text-align: center; }
  .facts-table tbody tr:first-child td { padding-top: 4px; }
  .facts-table td:first-child { text-align: left; font-weight: 700; width: 38%; }
  .facts-table tbody tr:last-child td { border-bottom: 0.7px solid var(--rule); padding-bottom: 3.5px; }
  .footnotes { margin-top: 5px; color: var(--ink-soft); line-height: 1.4; }

  .cautions { left: 13px; top: 151px; width: 80px; font-weight: 700; }
  .cautions p { margin-bottom: 3.4px; }
  .usage { left: 94px; top: 151px; width: 80px; }
  .usage .section-title { margin-bottom: 5px; }
  .usage p { margin-bottom: 7px; }
  .batch { left: 13px; top: 245px; font-family: "Josefin Sans", sans-serif; font-weight: 700; font-size: 5px; letter-spacing: 0.1em; }
  .more-info { left: 13px; top: 277px; font-family: "Josefin Sans", sans-serif; font-weight: 600; font-size: 4.6px; line-height: 1.5; letter-spacing: 0.03em; }
  .leaf-spot { position: absolute; left: 92px; top: 244px; width: 80px; height: 66px; }
</style>
</head>
<body>

<section class="label front-label">
  <svg class="front-art" viewBox="0 0 572 310" preserveAspectRatio="none">
    <defs>
      <radialGradient id="leafWashLeft" cx="0.5" cy="0.5" r="0.5">
        <stop offset="0" stop-color="#3f9444" stop-opacity="0.95"/>
        <stop offset="0.55" stop-color="#5aa64a" stop-opacity="0.75"/>
        <stop offset="0.85" stop-color="#9fd067" stop-opacity="0.35"/>
        <stop offset="1" stop-color="#9fd067" stop-opacity="0"/>
      </radialGradient>
      <radialGradient id="leafWashRight" cx="0.5" cy="0.5" r="0.5">
        <stop offset="0" stop-color="#3f9444" stop-opacity="0.9"/>
        <stop offset="0.6" stop-color="#5aa64a" stop-opacity="0.65"/>
        <stop offset="0.88" stop-color="#9fd067" stop-opacity="0.25"/>
        <stop offset="1" stop-color="#9fd067" stop-opacity="0"/>
      </radialGradient>
      <linearGradient id="leafEdge" x1="0" y1="0" x2="1" y2="0">
        <stop offset="0" stop-color="#4f9f47" stop-opacity="0.9"/>
        <stop offset="1" stop-color="#9fd067" stop-opacity="0"/>
      </linearGradient>
    </defs>
    <g role="img" aria-label="Watercolour hemp leaves fanning in from the left edge">
      <rect x="0" y="0" width="40" height="310" fill="url(#leafEdge)"/>
      <ellipse cx="60" cy="235" rx="200" ry="105" fill="url(#leafWashLeft)" transform="rotate(-22 60 235)"/>
      <ellipse cx="110" cy="120" rx="110" ry="40" fill="url(#leafWashLeft)" transform="rotate(-50 110 120)" opacity="0.8"/>
    </g>
    <g class="drips" stroke-linecap="round" fill="none">
      <line x1="264" y1="0" x2="264" y2="218" stroke="var(--drip-pale)" stroke-width="7" opacity="0.75"/>
      <line x1="298" y1="0" x2="298" y2="266" stroke="var(--drip-lime)" stroke-width="7" opacity="0.85"/>
      <line x1="315" y1="0" x2="315" y2="242" stroke="var(--drip-lime)" stroke-width="5" opacity="0.75"/>
      <line x1="338" y1="0" x2="338" y2="302" stroke="var(--drip-pale)" stroke-width="6" opacity="0.8"/>
      <line x1="378" y1="0" x2="378" y2="178" stroke="var(--drip-lime)" stroke-width="7" opacity="0.9"/>
      <line x1="388" y1="0" x2="388" y2="306" stroke="var(--drip-lime)" stroke-width="4" opacity="0.85"/>
      <line x1="426" y1="0" x2="426" y2="218" stroke="var(--drip-lime)" stroke-width="6" opacity="0.85"/>
      <line x1="443" y1="0" x2="443" y2="250" stroke="var(--drip-pale)" stroke-width="5" opacity="0.8"/>
    </g>
    <g role="img" aria-label="Watercolour hemp leaves rising from the lower right corner">
      <ellipse cx="500" cy="255" rx="130" ry="95" fill="url(#leafWashRight)" transform="rotate(-30 500 255)"/>
      <ellipse cx="555" cy="190" rx="40" ry="90" fill="url(#leafWashRight)" opacity="0.8"/>
    </g>
  </svg>
  <div class="front-text">
    <p class="kicker kicker-hemp">HEMP</p>
    <h1 class="brand-name">VELSORA</h1>
    <p class="kicker kicker-tincture">TINCTURE</p>
    <p class="product-lines">WHOLE HEMP AND COCONUT OIL<br>1000 MG CANNABIDOL</p>
  </div>
</section>

<section class="label back-label">
  <div class="block facts">
    <h2 class="section-title">SUPPLEMENT FACTS:</h2>
    <p class="serving"><span><b>Serving size:</b> 1/2 dropper (1ml)</span><b>Servings per container:</b> 60</p>
    <table class="facts-table">
      <thead>
        <tr><th></th><th>Amount per serving</th><th>% daily value</th></tr>
      </thead>
      <tbody>
        <tr><td>Calories</td><td>8</td><td></td></tr>
        <tr><td>Calories from fat</td><td>8</td><td></td></tr>
        <tr><td>Total fat</td><td>1g</td><td>2%*</td></tr>
        <tr><td>Hemp extract<br>(aerial parts)</td><td>15mg</td><td>**</td></tr>
      </tbody>
    </table>
    <p class="footnotes">*&nbsp;&nbsp; Percent daily values are based on a 2000 calorie diet.<br>**&nbsp; Daily value not established.</p>
  </div>

  <div class="block cautions">
    <p>Shake well before using.</p>
    <p>Store in a cool, dry place,<br>away from light</p>
    <p>Not to be used during<br>pregnancy or lactation.</p>
    <p>If you have a medical condition<br>or take pharmaceutical drugs,<br>please consult your Physician<br>before use.</p>
    <p>Keep out of reach of children.</p>
    <p>Do not use if safety seal<br>is broken or missing.</p>
  </div>

  <div class="block usage">
    <h2 class="section-title">SUGGESTED USE:</h2>
    <p>1/2 dropper per 100 lbs. as needed.</p>
    <h2 class="section-title">OTHER INGREDIENTS:</h2>
    <p>Coconut Oil (MCT),<br>Raw Coconut Oil.</p>
    <h2 class="section-title">MANUFACTURED BY:</h2>
    <p>Halden Botanics,<br>LLC Millbrook,<br>CO, 80412,<br>555 - 010 - 4821</p>
  </div>

  <p class="block batch">BATCH#: 031616</p>
  <p class="block more-info">For more information please visit:<br>www.haldenbotanics.com</p>

  <svg class="leaf-spot" viewBox="0 0 80 66" role="img" aria-label="Small watercolour hemp leaf">
    <defs>
      <radialGradient id="leafSmallWash" cx="0.5" cy="0.55" r="0.5">
        <stop offset="0" stop-color="#3f9444" stop-opacity="0.9"/>
        <stop offset="0.6" stop-color="#5aa64a" stop-opacity="0.6"/>
        <stop offset="1" stop-color="#9fd067" stop-opacity="0"/>
      </radialGradient>
    </defs>
    <ellipse cx="40" cy="36" rx="40" ry="30" fill="url(#leafSmallWash)"/>
  </svg>
</section>

</body>
</html>
```